Bramble Roofing Website Relaunch

We require a re-launch of our website, We are a longrun roofing company based in New Zealand, we are rapidly expanding and require a more professionally presented website our current website is www.brambleroofing.co.nz we want something modern, masculine and communicates a "strong" "superior" image, we already have a logo which I have attached we use the orange and silver one as you will see on our current website

Industry/Entity Type

It Company

Number of Pages Required

1 page

Colors
f37122
f78f20
000000
1b1b1b
474747
d3d3d3
f5f5f5

Requirements
Must have
• Images of our work
• Email and Mobile Contact Details
• Link to Facebook page
• Who We Are, What We Do
• Certified Trade Craftsman Logo
• Our Logo

```html
<!DOCTYPE html>
<html lang="en">
<head>
<meta charset="utf-8">
<title>Bramble Roofing</title>
<link href="https://fonts.googleapis.com/css2?family=Exo+2:wght@500;600;700&family=Lato:ital,wght@0,400;0,700;1,400&display=swap" rel="stylesheet">
<style>
:root{
  --orange:#f37122;
  --orange-light:#f78f20;
  --black:#000000;
  --ink:#1b1b1b;
  --charcoal:#474747;
  --silver:#d3d3d3;
  --mist:#f5f5f5;
  --card:#5a5a5a;
  --footer:#2c2c2c;
  --text:#3a3a3a;
}
*{box-sizing:border-box;margin:0;padding:0}
html,body{width:1200px;height:3000px;overflow:hidden;background:#fff}
body{position:relative;font-family:"Lato",Arial,sans-serif;color:var(--text)}
a{text-decoration:none}
.abs{position:absolute}
.heading{font-family:"Exo 2",Arial,sans-serif;font-weight:600;text-transform:uppercase;font-size:34px;letter-spacing:.5px;text-align:center;color:var(--charcoal);width:1200px;left:0}
.heading .accent{color:var(--orange)}
.heading.light{color:#fff}

/* header */
.hero-photo{left:0;top:0;width:1200px;height:575px;background:linear-gradient(180deg,#c4d5e6 0%,#9db4cc 22%,#59626c 36%,#2c2f33 48%,#34373a 66%,#6e5a3c 72%,#5f8a34 80%,#4a7526 100%)}
.site-header{left:0;top:0;width:1200px;height:105px;background:rgba(255,255,255,.92)}
.brand{left:162px;top:26px;display:flex;align-items:center;gap:14px}
.brand-mark{width:52px;height:52px;background:var(--orange)}
.brand-name{font-family:"Exo 2",Arial,sans-serif;font-weight:700;font-size:26px;color:var(--orange);line-height:1;text-transform:uppercase;width:150px}
.top-contact{top:20px;display:flex;align-items:center;gap:10px;font-size:14px;color:var(--charcoal)}
.main-nav{left:600px;top:68px;display:flex;font-family:"Exo 2",Arial,sans-serif;font-weight:600;font-size:15px;color:var(--ink)}
.main-nav a{color:inherit;padding:0 19px}
.main-nav a.active{color:var(--orange)}
.hero-title{left:162px;top:482px;font-family:"Exo 2",Arial,sans-serif;font-weight:700;font-size:26px;line-height:36px;color:#fff;text-transform:uppercase;text-shadow:0 2px 4px rgba(0,0,0,.6)}

/* about */
.about-text{left:165px;top:705px;width:870px;font-size:13px;line-height:21px;text-align:center;color:var(--text)}
.btn{display:flex;align-items:center;justify-content:center;background:linear-gradient(180deg,var(--orange-light),#d25a18);color:#fff;font-family:"Exo 2",Arial,sans-serif;font-weight:700;font-size:14px;text-transform:uppercase;height:30px;text-decoration:none}
.btn-about{left:534px;top:812px;width:124px;padding-right:14px}
.btn-tip{position:absolute;right:-16px;top:0;width:30px;height:30px}

/* services */
.services-band{left:0;top:888px;width:1200px;height:290px;background:linear-gradient(180deg,#5d5d5d,#3f3f3f)}
.services-lower{left:0;top:1178px;width:1200px;height:242px;background:#eeeeee}
.service-card{top:1010px;width:282px;height:355px;background:var(--card)}
.service-photo{width:282px;height:166px}
.service-icon{position:absolute;left:111px;top:130px;width:60px;height:70px}
.service-title{position:absolute;top:222px;width:100%;text-align:center;font-family:"Exo 2",Arial,sans-serif;font-weight:600;font-size:18px;color:#fff;text-transform:uppercase}
.service-rule{position:absolute;top:254px;left:111px;width:60px;height:2px;background:var(--orange)}
.service-text{position:absolute;top:270px;left:22px;width:238px;text-align:center;font-size:13px;line-height:20px;color:#eee}
.service-more{position:absolute;left:126px;bottom:-15px;width:30px;height:30px}

/* gallery */
.hex{width:152px;height:176px;clip-path:polygon(50% 0,100% 25%,100% 75%,50% 100%,0 75%,0 25%);background:#4a4a4a}
.hex-photo{position:absolute;inset:3px;clip-path:polygon(50% 0,100% 25%,100% 75%,50% 100%,0 75%,0 25%)}
.hex-caption{position:absolute;inset:0;display:flex;flex-direction:column;align-items:center;justify-content:flex-end;padding-bottom:28px;color:#fff;font-family:"Exo 2",Arial,sans-serif;font-weight:600;font-size:15px;background:rgba(40,40,40,.45)}
.hex-view{background:var(--orange)}
.hex-view .hex-photo{background:#fff}
.view-all{position:absolute;left:10px;top:62px;width:132px;height:52px;font-size:14px;line-height:18px;text-align:center}

/* testimonials */
.testimonial-band{left:0;top:1920px;width:1200px;height:445px;background:linear-gradient(180deg,#4c4c4c,#2f2f2f)}
.testimonial-card{left:225px;top:1985px;width:750px;height:310px;background:rgba(235,235,235,.93)}
.stars{position:absolute;left:320px;top:84px;display:flex;gap:10px}
.quote-text{position:absolute;left:70px;top:120px;width:610px;font-style:italic;font-size:13px;line-height:20px;text-align:center;color:var(--ink)}
.quote-mark{position:absolute;left:0;width:100%;top:208px;text-align:center;font-family:"Exo 2",Arial,sans-serif;font-weight:700;font-size:44px;color:var(--charcoal);line-height:40px}
.quote-name{position:absolute;left:0;width:100%;top:254px;text-align:center;font-family:"Exo 2",Arial,sans-serif;font-weight:700;font-size:16px;color:var(--orange);text-transform:uppercase}
.slider-arrow{top:2118px;width:44px;height:50px}

/* inquiry */
.field{height:38px;border:1px solid var(--silver);background:#fff;font-size:13px;color:#555;padding:10px 14px}
.field-icon{position:absolute;right:0;top:0;width:38px;height:100%;border-left:1px solid var(--silver);display:flex;align-items:center;justify-content:center}
.btn-send{left:544px;top:2636px;width:100px;height:32px;font-size:15px;padding-right:14px}

/* footer */
.site-footer{left:0;top:2730px;width:1200px;height:230px;background:var(--footer)}
.footer-title{font-family:"Exo 2",Arial,sans-serif;font-weight:600;font-size:18px;color:#fff;text-transform:uppercase}
.footer-text{font-size:13px;line-height:20px;color:#e3e3e3}
.footer-divider{top:2772px;width:1px;height:150px;background:#555}
.footer-link{font-family:"Exo 2",Arial,sans-serif;font-weight:600;font-size:14px;color:var(--orange);text-transform:uppercase}
.badge-panel{left:510px;top:2818px;width:224px;height:86px;background:#fff;display:flex;align-items:center;justify-content:center;gap:12px}
.badge{width:60px;height:60px;border-radius:50%}
.office-row{display:flex;align-items:flex-start;gap:12px;font-size:13px;line-height:20px;color:#e3e3e3}
.bottom-bar{left:0;top:2960px;width:1200px;height:40px;background:var(--ink)}
.bottom-orange{left:0;top:2960px;width:1040px;height:40px;background:var(--orange);clip-path:polygon(0 0,1000px 0,100% 100%,0 100%)}
.copyright{left:162px;top:2973px;font-size:11px;color:#fff;text-transform:uppercase;font-weight:700}
.follow{left:832px;top:2969px;display:flex;align-items:center;gap:10px;font-size:12px;color:#fff}
.social-dot{width:22px;height:22px;border-radius:50%;border:2px solid #fff}
</style>
</head>
<body>

<!-- Hero -->
<div class="abs hero-photo" role="img" aria-label="Photo of a dark weatherboard house with a long-run steel roof, a timber deck and a green lawn"></div>

<header class="abs site-header">
  <div class="abs brand">
    <span class="brand-mark"></span>
    <span class="brand-name">Bramble Roofing</span>
  </div>
  <div class="abs top-contact" style="left:756px">
    <svg width="22" height="22" viewBox="0 0 24 24" fill="none" stroke="#f37122" stroke-width="2"><path d="M5 3h4l2 5-3 2a11 11 0 0 0 6 6l2-3 5 2v4a2 2 0 0 1-2 2A17 17 0 0 1 3 5a2 2 0 0 1 2-2z"/></svg>
    <span>021 555 01942</span>
  </div>
  <div class="abs top-contact" style="left:904px;font-size:12px">
    <svg width="24" height="18" viewBox="0 0 24 18" fill="none" stroke="#f37122" stroke-width="2"><rect x="1" y="1" width="22" height="16"/><path d="M1 1l11 9 11-9"/></svg>
    <span>hello@brambleroofing.co.nz</span>
  </div>
  <nav class="abs main-nav">
    <a class="active" href="#">HOME</a>
    <a href="#">ABOUT US</a>
    <a href="#">SERVICES</a>
    <a href="#">OUR WORK</a>
    <a href="#">CONTACT</a>
  </nav>
</header>

<h1 class="abs hero-title">Leaders in all long run coated steel,<br>Zincara installations &amp; roofing solutions</h1>

<!-- About -->
<h2 class="abs heading" style="top:642px"><span class="accent">About</span> Bramble Roofing</h2>
<p class="abs about-text">We are a local, family owned and operated company with over 18 years extensive experience in the roofing industry, Roofing not only Waikato and Auckland but surrounding areas also. We are committed to providing superior service to our customers regardless of how big or small your project is, Your satisfaction is our guarantee. We take pride in installing quality products, Offering a workmanship guarantee and manufacturers material warranties where applicable. In a fast paced advancing industry we are constantly striving to provide the latest, modern quality installation</p>
<a class="abs btn btn-about" href="#">Read More
  <svg class="btn-tip" viewBox="0 0 30 30"><polygon points="15,1 29,15 15,29 1,15" fill="#fff" stroke="#f37122" stroke-width="2"/><path d="M11 15h8M16 11l4 4-4 4" stroke="#f37122" stroke-width="2" fill="none"/></svg>
</a>

<!-- Services -->
<div class="abs services-band" role="img" aria-label="Muted photo of a house under construction wrapped in scaffolding"></div>
<div class="abs services-lower"></div>
<h2 class="abs heading light" style="top:934px"><span class="accent">Our</span> Services</h2>

<article class="abs service-card" style="left:162px">
  <div class="service-photo" role="img" aria-label="Photo of a finished residential home with a dark roof" style="background:linear-gradient(180deg,#8fb0d4 0%,#a8c2dc 40%,#2f3136 60%,#3d6b2a 100%)"></div>
  <svg class="service-icon" viewBox="0 0 60 70"><polygon points="30,2 58,18 58,52 30,68 2,52 2,18" fill="#fff" stroke="#f37122" stroke-width="3"/><path d="M16 36l14-12 14 12v12H16z" fill="#1b1b1b"/><rect x="27" y="40" width="6" height="8" fill="#fff"/></svg>
  <h3 class="service-title">Residential</h3>
  <div class="service-rule"></div>
  <p class="service-text">Lorem ipsum dolor sit amet, consectetuer adipiscing elit, sed diam nonummy nibh euismod tincidunt ut laoreet</p>
  <svg class="service-more" viewBox="0 0 30 30"><polygon points="15,1 28,8 28,22 15,29 2,22 2,8" fill="#5a5a5a"/><path d="M15 9v12M9 15h12" stroke="#f37122" stroke-width="3"/></svg>
</article>

<article class="abs service-card" style="left:458px">
  <div class="service-photo" role="img" aria-label="Photo of a large industrial building with a new steel roof" style="background:linear-gradient(180deg,#c9d3df 0%,#b8c3cf 35%,#5a5e66 55%,#c9b6a8 100%)"></div>
  <svg class="service-icon" viewBox="0 0 60 70"><polygon points="30,2 58,18 58,52 30,68 2,52 2,18" fill="#fff" stroke="#f37122" stroke-width="3"/><path d="M15 48V32l8 5v-5l8 5v-5l8 5V22h5v26z" fill="#1b1b1b"/></svg>
  <h3 class="service-title">Industrial</h3>
  <div class="service-rule"></div>
  <p class="service-text">Lorem ipsum dolor sit amet, consectetuer adipiscing elit, sed diam nonummy nibh euismod tincidunt ut laoreet</p>
  <svg class="service-more" viewBox="0 0 30 30"><polygon points="15,1 28,8 28,22 15,29 2,22 2,8" fill="#5a5a5a"/><path d="M15 9v12M9 15h12" stroke="#f37122" stroke-width="3"/></svg>
</article>

<article class="abs service-card" style="left:756px">
  <div class="service-photo" role="img" aria-label="Photo of a commercial building frame with scaffolding" style="background:linear-gradient(180deg,#dfe6ee 0%,#c9d2dc 40%,#5c6068 65%,#9a9a9a 100%)"></div>
  <svg class="service-icon" viewBox="0 0 60 70"><polygon points="30,2 58,18 58,52 30,68 2,52 2,18" fill="#fff" stroke="#f37122" stroke-width="3"/><rect x="20" y="20" width="20" height="30" fill="#1b1b1b"/><g fill="#fff"><rect x="24" y="24" width="4" height="4"/><rect x="32" y="24" width="4" height="4"/><rect x="24" y="32" width="4" height="4"/><rect x="32" y="32" width="4" height="4"/><rect x="27" y="42" width="6" height="8"/></g></svg>
  <h3 class="service-title">Commercial</h3>
  <div class="service-rule"></div>
  <p class="service-text">Lorem ipsum dolor sit amet, consectetuer adipiscing elit, sed diam nonummy nibh euismod tincidunt ut laoreet</p>
  <svg class="service-more" viewBox="0 0 30 30"><polygon points="15,1 28,8 28,22 15,29 2,22 2,8" fill="#5a5a5a"/><path d="M15 9v12M9 15h12" stroke="#f37122" stroke-width="3"/></svg>
</article>

<!-- Work gallery -->
<h2 class="abs heading" style="top:1462px"><span class="accent">Work</span> Gallery</h2>

<div class="abs hex" style="left:250px;top:1524px">
  <div class="hex-photo" role="img" aria-label="Photo of a roof under construction" style="background:linear-gradient(180deg,#bfc8d2,#6a6e74 55%,#8b8d8f)"></div>
  <div class="hex-caption">TITLE - 1
    <svg width="22" height="22" viewBox="0 0 22 22" style="margin-top:8px"><path d="M11 3v16M3 11h16" stroke="#f37122" stroke-width="3"/></svg>
  </div>
</div>
<div class="abs hex" style="left:432px;top:1524px"><div class="hex-photo" role="img" aria-label="Photo of a green steel-clad shed" style="background:linear-gradient(180deg,#aebccb,#3c5a44 55%,#2d3b30)"></div></div>
<div class="abs hex" style="left:614px;top:1524px"><div class="hex-photo" role="img" aria-label="Photo of a house with autumn trees" style="background:linear-gradient(180deg,#c8d2dc,#7b5a3c 50%,#4a4a48)"></div></div>
<div class="abs hex" style="left:796px;top:1524px"><div class="hex-photo" role="img" aria-label="Photo of a modern building with dark cladding" style="background:linear-gradient(180deg,#d4dce4,#3b3e42 50%,#6d8a5a)"></div></div>

<div class="abs hex" style="left:158px;top:1690px"><div class="hex-photo" role="img" aria-label="Photo of a new white house" style="background:linear-gradient(180deg,#9fb7cf,#dfe3e6 50%,#5d7e44)"></div></div>
<div class="abs hex" style="left:342px;top:1690px"><div class="hex-photo" role="img" aria-label="Photo of a building framed in scaffolding" style="background:linear-gradient(180deg,#c9d4de,#5c6066 50%,#8e8f90)"></div></div>
<div class="abs hex hex-view" style="left:524px;top:1690px">
  <div class="hex-photo"></div>
  <a class="btn view-all" href="#">View All<br>Work Gallery</a>
</div>
<div class="abs hex" style="left:706px;top:1690px"><div class="hex-photo" role="img" aria-label="Photo of a large open-sided shed at dusk" style="background:linear-gradient(180deg,#c7b8a8,#2a2522 45%,#6b5540)"></div></div>
<div class="abs hex" style="left:888px;top:1690px"><div class="hex-photo" role="img" aria-label="Photo of a house with building wrap" style="background:linear-gradient(180deg,#c3ccd6,#4e5054 45%,#d0c8c4)"></div></div>

<!-- Testimonials -->
<div class="abs testimonial-band" role="img" aria-label="Muted photo of a building site with scaffolding"></div>
<div class="abs testimonial-card">
  <h2 class="heading" style="position:absolute;top:22px;width:750px"><span class="accent">Client</span> Testimonials</h2>
  <div class="stars">
    <svg width="14" height="14" viewBox="0 0 20 20"><polygon points="10,1 12.6,7.2 19,7.6 14,11.8 15.6,18.5 10,14.8 4.4,18.5 6,11.8 1,7.6 7.4,7.2" fill="#f37122"/></svg>
    <svg width="14" height="14" viewBox="0 0 20 20"><polygon points="10,1 12.6,7.2 19,7.6 14,11.8 15.6,18.5 10,14.8 4.4,18.5 6,11.8 1,7.6 7.4,7.2" fill="#f37122"/></svg>
    <svg width="14" height="14" viewBox="0 0 20 20"><polygon points="10,1 12.6,7.2 19,7.6 14,11.8 15.6,18.5 10,14.8 4.4,18.5 6,11.8 1,7.6 7.4,7.2" fill="#f37122"/></svg>
    <svg width="14" height="14" viewBox="0 0 20 20"><polygon points="10,1 12.6,7.2 19,7.6 14,11.8 15.6,18.5 10,14.8 4.4,18.5 6,11.8 1,7.6 7.4,7.2" fill="#f37122"/></svg>
    <svg width="14" height="14" viewBox="0 0 20 20"><polygon points="10,1 12.6,7.2 19,7.6 14,11.8 15.6,18.5 10,14.8 4.4,18.5 6,11.8 1,7.6 7.4,7.2" fill="#f37122"/></svg>
  </div>
  <p class="quote-text">Helena is Callum's wife and office manager, she works full time off site, with an employment history of 15+ years in the construction, materials handling equipment and project administration sectors. Her spare time is taken up managing Bramble Roofing, facilitating the daily operations, many clerical positions, health and safety and ensuring client enquires are responded too timely.</p>
  <div class="quote-mark">&ldquo;</div>
  <div class="quote-name">Helena Marsh</div>
</div>
<svg class="abs slider-arrow" style="left:116px" viewBox="0 0 44 50"><polygon points="22,2 42,13 42,37 22,48 2,37 2,13" fill="none" stroke="#fff" stroke-width="2"/><path d="M25 16l-9 9 9 9" stroke="#fff" stroke-width="3" fill="none"/></svg>
<svg class="abs slider-arrow" style="left:1036px" viewBox="0 0 44 50"><polygon points="22,2 42,13 42,37 22,48 2,37 2,13" fill="none" stroke="#f37122" stroke-width="2"/><path d="M19 16l9 9-9 9" stroke="#f37122" stroke-width="3" fill="none"/></svg>

<!-- Quick inquiry -->
<h2 class="abs heading" style="top:2408px"><span class="accent">Quick</span> Inquiry</h2>
<form>
  <div class="abs field" style="left:220px;top:2478px;width:370px">Name
    <span class="field-icon"><svg width="18" height="18" viewBox="0 0 20 20" fill="none" stroke="#f37122" stroke-width="1.8"><circle cx="10" cy="6" r="4"/><path d="M2 19a8 8 0 0 1 16 0"/></svg></span></div>
  <div class="abs field" style="left:220px;top:2528px;width:370px">Company
    <span class="field-icon"><svg width="18" height="18" viewBox="0 0 20 20" fill="none" stroke="#f37122" stroke-width="1.8"><rect x="5" y="2" width="10" height="16"/><path d="M8 6h4M8 10h4M9 18v-4h2v4"/></svg></span></div>
  <div class="abs field" style="left:220px;top:2580px;width:370px">Email
    <span class="field-icon"><svg width="18" height="14" viewBox="0 0 24 18" fill="none" stroke="#f37122" stroke-width="2"><rect x="1" y="1" width="22" height="16"/><path d="M1 1l11 9 11-9"/></svg></span></div>
  <div class="abs field" style="left:605px;top:2478px;width:375px">Subject
    <span class="field-icon"><svg width="18" height="18" viewBox="0 0 20 20" fill="none" stroke="#f37122" stroke-width="1.8"><path d="M3 17l4-1 10-10-3-3L4 13z"/></svg></span></div>
  <div class="abs field" style="left:605px;top:2528px;width:375px;height:88px">Message
    <span class="field-icon" style="align-items:flex-start;padding-top:10px;border-left:none"><svg width="18" height="18" viewBox="0 0 20 20" fill="none" stroke="#f37122" stroke-width="1.8"><path d="M3 17l1-4 10-10 3 3-10 10zM12 5l3 3"/></svg></span></div>
  <a class="abs btn btn-send" href="#">Send
    <svg class="btn-tip" style="width:32px;height:32px" viewBox="0 0 30 30"><polygon points="15,1 29,15 15,29 1,15" fill="#fff" stroke="#f37122" stroke-width="2"/><path d="M11 15h8M16 11l4 4-4 4" stroke="#f37122" stroke-width="2" fill="none"/></svg>
  </a>
</form>

<!-- Footer -->
<footer class="abs site-footer"></footer>
<div class="abs" style="left:162px;top:2774px;width:270px">
  <h3 class="footer-title">Lorem Ipsum Dolor</h3>
  <p class="footer-text" style="margin-top:12px">Lorem ipsum dolor sit amet, consectetuer adipiscing elit, sed diam nonummy nibh euismod tincidunt ut laoreet dolore.</p>
  <p class="footer-link" style="margin-top:12px">Contact Us Today</p>
</div>
<div class="abs footer-divider" style="left:458px"></div>
<h3 class="abs footer-title" style="left:510px;top:2774px">Our Accreditations</h3>
<div class="abs badge-panel" aria-label="Accreditation badges">
  <span class="badge" style="background:#2b2b2b"></span>
  <span class="badge" style="background:#b89a4c"></span>
  <span class="badge" style="background:#2e3d8f"></span>
</div>
<div class="abs footer-divider" style="left:772px"></div>
<div class="abs" style="left:828px;top:2774px;width:240px">
  <h3 class="footer-title">Our Office</h3>
  <div class="office-row" style="margin-top:14px">
    <svg width="16" height="22" viewBox="0 0 16 22"><path d="M8 0a8 8 0 0 0-8 8c0 6 8 14 8 14s8-8 8-14a8 8 0 0 0-8-8z" fill="#f37122"/><circle cx="8" cy="8" r="3" fill="#2c2c2c"/></svg>
    <span>16 Lorem ipsum dolor sit amet<br>sed beneti, Street No-123456</span>
  </div>
  <div class="office-row" style="margin-top:8px">
    <svg width="16" height="16" viewBox="0 0 24 24" fill="none" stroke="#f37122" stroke-width="2.4"><path d="M5 3h4l2 5-3 2a11 11 0 0 0 6 6l2-3 5 2v4a2 2 0 0 1-2 2A17 17 0 0 1 3 5a2 2 0 0 1 2-2z"/></svg>
    <span>021 555 01942</span>
  </div>
  <div class="office-row" style="margin-top:8px;font-size:12px">
    <svg width="16" height="12" viewBox="0 0 24 18" fill="none" stroke="#f37122" stroke-width="2.4"><rect x="1" y="1" width="22" height="16"/><path d="M1 1l11 9 11-9"/></svg>
    <span>hello@brambleroofing.co.nz</span>
  </div>
</div>

<div class="abs bottom-bar"></div>
<div class="abs bottom-orange"></div>
<p class="abs copyright">Copyright &copy; 2017 Bramble Roofing. All rights reserved.</p>
<div class="abs follow"><span>Follow Us</span><span class="social-dot"></span></div>

</body>
</html>
```